Medical Professionals- Financial services

We need a logo and stationery designed for a company called Vantor Crest Capital. Based in Queensland Australia, we provide financial services and planning for medical professionals. This includes all aspects of their financial life including Debt, Wealth accumulation, Risk management and ad hoc financial services including legal and accounting.

We do not have any specific requirements for stationery itself, anything that looks quite corporate would be great.

We need stationery for the following
- Business Cards- back
- With compliments
- Letter head
- Email signature
- Display folder

Please note there must be an accredited by KOA logo on all stationery

Must also include "Vantor Crest capital Authorised Representative of Klyde Ostrand Advisory Pty Ltd AFS Licensee no. 518349"

EXCEPTIONS for the business card

Small written, can be anywhere.

Target Market(s)

Medical Professionals- Specialist doctors, Surgeons

Industry/Entity Type

Business

Requirements
Must have
• Must incorporate a medical logo (cross or Caduceus) in a smart way. We would like to see a corporate style logo that will attract to specialist doctors and surgeons.
Nice to have
• Would like to see a corporate style logo

```html
<!DOCTYPE html>
<html lang="en">
<head>
<meta charset="utf-8">
<title>Vantor Crest Capital — Stationery Set</title>
<link rel="stylesheet" href="https://fonts.googleapis.com/css2?family=Open+Sans:wght@400;600;700&display=swap">
<style>
  :root{
    --green:#1c9e36;
    --green-bright:#33c443;
    --green-soft:#5cc86b;
    --ink:#333333;
    --ink-soft:#555555;
    --silver:#d6d6d6;
    --silver-dark:#b8b8b8;
    --paper:#ffffff;
    --board-light:#ececec;
    --board-dark:#4d4d4d;
    --badge:#2a7fa8;
  }
  *{margin:0;padding:0;box-sizing:border-box}
  html,body{width:1200px;height:1115px;overflow:hidden}
  body{
    font-family:"Open Sans",Arial,sans-serif;
    color:var(--ink);
    background:radial-gradient(ellipse 70% 75% at 50% 55%,var(--board-light) 0%,#bcbcbc 55%,var(--board-dark) 100%);
    position:relative;
  }
  .piece{position:absolute;background:var(--paper);overflow:hidden;box-shadow:0 2px 6px rgba(0,0,0,.25)}
  .piece > svg.art{position:absolute;inset:0;width:100%;height:100%}
  .brand{position:absolute;display:flex;align-items:center;gap:8px;color:var(--ink-soft);font-weight:400;line-height:1.05;white-space:nowrap}
  .brand-square{background:var(--green);flex:none}
  .brand-name span{display:block}
  .brand-light{color:#fff}
  .accreditation{position:absolute;font-size:6.5px;line-height:1.3;color:var(--ink-soft);text-align:right}
  .accreditation .badge{display:inline-block;width:62px;height:11px;background:var(--badge);border-radius:2px;margin-bottom:2px}
  .accreditation.left{text-align:left}
  .contact-row{position:absolute;display:flex;font-size:9px;line-height:1.25;color:var(--ink-soft);white-space:nowrap}
  .contact-row .col{padding:0 12px;border-left:2px solid var(--green)}
  .contact-row .col:first-child{border-left:none;text-align:right}
  .person{position:absolute;text-align:right}
  .person .name{font-weight:700;font-size:17px;color:var(--ink)}
  .person .role{font-size:12px;color:var(--ink-soft)}

  /* folder */
  .folder{left:48px;top:100px;width:479px;height:627px}

  /* letterhead */
  .letterhead{left:563px;top:35px;width:587px;height:755px}
  .letter-body{position:absolute;left:52px;top:163px;width:508px;font-size:11.9px;line-height:16.2px;letter-spacing:-0.1px;color:#222}
  .letter-body .salutation{font-size:14px;margin-bottom:19px}
  .letter-body p{text-align:justify;margin-bottom:16px}
  .signature{position:absolute;left:295px;top:600px;width:135px;height:58px;border-radius:28px;background:linear-gradient(90deg,rgba(30,60,150,.18),rgba(30,60,150,.05))}
  .letter-strip{position:absolute;left:0;bottom:0;width:100%;height:5px;display:flex}
  .letter-strip i{flex:1}

  /* compliments slip */
  .compliments{left:42px;top:766px;width:485px;height:100px}

  /* envelope */
  .envelope{left:43px;top:910px;width:314px;height:155px}
  .window{position:absolute;left:163px;top:98px;width:123px;height:42px;border:1px solid #777;border-radius:6px;background:#fff}
  .return-address{position:absolute;left:11px;top:116px;font-size:5.5px;line-height:1.35;color:var(--ink-soft)}
  .return-address b{font-weight:400;font-size:6.5px}

  /* disc */
  .disc{left:398px;top:890px;width:162px;height:162px;border-radius:50%;box-shadow:0 2px 6px rgba(0,0,0,.3)}
  .disc-hub{position:absolute;left:66px;top:62px;width:46px;height:46px;border-radius:50%;background:#fff;display:flex;align-items:center;justify-content:center}
  .disc-hub i{width:30px;height:30px;border-radius:50%;background:#666}

  /* cards */
  .card-front{left:651px;top:886px;width:234px;height:134px}
  .card-back{left:931px;top:886px;width:233px;height:134px}
  .card-url{position:absolute;right:5px;bottom:4px;font-size:6px;color:#fff}
</style>
</head>
<body>

<!-- Display folder -->
<section class="piece folder" aria-label="Display folder">
  <svg class="art" viewBox="0 0 479 627" preserveAspectRatio="none">
    <defs>
      <linearGradient id="folderSilver" x1="0" y1="0" x2="1" y2="1">
        <stop offset="0" stop-color="#ffffff"/><stop offset=".5" stop-color="#d2d2d2"/><stop offset="1" stop-color="#f2f2f2"/>
      </linearGradient>
      <radialGradient id="folderGreen" cx=".5" cy=".55" r=".6">
        <stop offset="0" stop-color="var(--green-bright)"/><stop offset="1" stop-color="var(--green)"/>
      </radialGradient>
    </defs>
    <path d="M140 0 C260 40 420 120 479 200 L479 0 Z" fill="url(#folderSilver)" opacity=".8"/>
    <path d="M0 330 C80 180 200 90 330 0 L380 0 C250 90 120 200 0 420 Z" fill="url(#folderSilver)" opacity=".7"/>
    <path d="M0 627 L0 450 C140 330 320 270 479 240 L479 627 Z" fill="url(#folderGreen)"/>
    <path d="M360 627 C420 520 460 420 479 360 L479 627 Z" fill="url(#folderSilver)"/>
  </svg>
  <div class="brand" style="left:36px;top:200px">
    <i class="brand-square" style="width:40px;height:40px"></i>
    <div class="brand-name"><span style="font-size:40px">Vantor Crest</span><span style="font-size:25px;padding-left:20px">Capital</span></div>
  </div>
  <div class="accreditation left" style="left:30px;top:585px;color:#fff">
    <span class="badge"></span><br>
    Authorised Representative of Klyde Ostrand Advisory Pty Ltd AFS Licensee no. 518349
  </div>
</section>

<!-- Letterhead -->
<section class="piece letterhead" aria-label="Letterhead">
  <svg class="art" viewBox="0 0 587 755" preserveAspectRatio="none">
    <defs>
      <linearGradient id="letterGreen" x1="0" y1="1" x2="1" y2="0">
        <stop offset="0" stop-color="var(--green)"/><stop offset=".5" stop-color="var(--green-bright)"/><stop offset="1" stop-color="var(--green)"/>
      </linearGradient>
    </defs>
    <path d="M0 290 C150 220 300 150 430 110 L587 90 L587 120 C430 150 250 230 0 330 Z" fill="#eeeeee"/>
    <path d="M0 755 L0 560 C140 420 360 320 587 280 L587 755 Z" fill="url(#letterGreen)" opacity=".72"/>
    <path d="M400 755 C470 620 540 520 587 470 L587 755 Z" fill="#e4e4e4" opacity=".9"/>
  </svg>
  <div class="brand" style="left:52px;top:30px">
    <i class="brand-square" style="width:26px;height:26px"></i>
    <div class="brand-name"><span style="font-size:25px">Vantor Crest</span><span style="font-size:15px;padding-left:10px">Capital</span></div>
  </div>
  <div class="accreditation" style="right:27px;top:33px">
    <span class="badge" style="width:92px"></span><br>
    Authorised Representative of Klyde Ostrand<br>Advisory Pty Ltd AFS Licensee no. 518349
  </div>
  <div class="letter-body">
    <div class="salutation">Dear sir / madame</div>
    <p>A news article discusses current or recent news of either general interest (i.e. daily newspapers) or of a specific topic (i.e. political or trade news magazines, club newsletters, or technology news websites).</p>
    <p>A news article can include accounts of eye witnesses to the happening event. It can contain photographs, accounts, statistics, graphs, recollections, interviews, polls, debates on the topic, etc. Headlines can be used to focus the reader's attention on a particular (or main) part of the article. The writer can also give facts and detailed information following answers to general questions like who, what, when, where, why and how.</p>
    <p>Quoted references can also be helpful. References to people can also be made through written accounts of interviews and debates confirming the factuality of the writer's information and the reliability of his source. The writer can use redirection to ensure that the reader keeps reading the article and to draw her attention to other articles. For example, phrases like "Continued on page 3" redirect the reader to a page where the article is continued.</p>
    <p>While a good conclusion is an important ingredient for newspaper articles, the immediacy of a deadline environment means that copy editing often takes the form of deleting everything past an arbitrary point in the story corresponding to the dictates of available space on a page. Therefore, newspaper reporters are trained to write in inverted pyramid style, with all the most important information in the first paragraph or two. If less vital details are pushed towards the end of the story, the potentially destructive impact of draconian copy editing will be minimized.</p>
  </div>
  <div class="signature" role="img" aria-label="Handwritten signature"></div>
  <div class="person" style="right:27px;top:594px">
    <div class="name">Marcus Hale</div>
    <div class="role">Executive</div>
  </div>
  <div class="contact-row" style="right:18px;top:718px">
    <div class="col">00, Address Line<br>Address Line 2</div>
    <div class="col">Phone: 000 XXX 0000<br>Fax: 000 XXX 0000</div>
    <div class="col">info@website.com<br>www.website.com</div>
  </div>
  <div class="letter-strip"><i style="background:var(--green-bright)"></i><i style="background:var(--green)"></i></div>
</section>

<!-- With compliments slip -->
<section class="piece compliments" aria-label="With compliments slip">
  <div class="brand" style="left:8px;top:7px">
    <i class="brand-square" style="width:20px;height:20px"></i>
    <div class="brand-name"><span style="font-size:18px">Vantor Crest</span><span style="font-size:11px;padding-left:8px">Capital</span></div>
  </div>
  <div class="person" style="right:16px;top:16px">
    <div class="name">Marcus Hale</div>
    <div class="role">Executive</div>
  </div>
  <div class="contact-row" style="left:-7px;top:72px">
    <div class="col">00, Address Line<br>Address Line 2</div>
    <div class="col">Phone: 000 XXX 0000<br>Fax: 000 XXX 0000</div>
    <div class="col">info@websitecom<br>www.websitecom</div>
  </div>
  <div class="accreditation" style="right:12px;top:64px;font-size:5px">
    <span class="badge" style="width:80px;height:10px"></span><br>
    Authorised Representative of Klyde Ostrand<br>Advisory Pty Ltd AFS Licensee no. 518349
  </div>
  <div style="position:absolute;left:0;bottom:0;width:100%;height:3px;display:flex"><i style="flex:1;background:var(--green-bright)"></i><i style="flex:1;background:var(--green)"></i></div>
</section>

<!-- Envelope -->
<section class="piece envelope" aria-label="Envelope">
  <svg class="art" viewBox="0 0 314 155" preserveAspectRatio="none">
    <defs>
      <linearGradient id="envGreen" x1="0" y1="0" x2="1" y2="0">
        <stop offset="0" stop-color="var(--green)"/><stop offset=".5" stop-color="var(--green-bright)"/><stop offset="1" stop-color="var(--green)"/>
      </linearGradient>
    </defs>
    <path d="M230 155 C270 110 300 80 314 70 L314 155 Z" fill="#dcdcdc"/>
    <path d="M0 0 L314 0 L314 60 C220 72 120 65 0 75 Z" fill="url(#envGreen)"/>
  </svg>
  <div class="brand brand-light" style="left:10px;top:10px">
    <i class="brand-square" style="width:18px;height:18px;background:#fff"></i>
    <div class="brand-name"><span style="font-size:15px">Vantor Crest</span><span style="font-size:9px;padding-left:8px">Capital</span></div>
  </div>
  <div class="return-address"><b>Vantor Crest Capital</b><br>00, Address Line<br>Address Line 2<br>www.website.com</div>
  <div class="window"></div>
</section>

<!-- Disc -->
<section class="piece disc" aria-label="Disc label">
  <svg class="art" viewBox="0 0 162 162">
    <path d="M0 0 L162 0 L162 95 C120 90 60 100 0 130 Z" fill="var(--green)"/>
    <path d="M30 0 C60 40 110 60 162 70 L162 0 Z" fill="var(--green-bright)" opacity=".6"/>
    <path d="M0 60 C30 80 60 120 80 162 L0 162 Z" fill="#d8d8d8" opacity=".8"/>
  </svg>
  <div class="disc-hub"><i></i></div>
  <div class="brand" style="left:58px;top:138px;gap:3px">
    <i class="brand-square" style="width:8px;height:8px"></i>
    <div class="brand-name"><span style="font-size:8px">Vantor Crest</span><span style="font-size:5px">Capital</span></div>
  </div>
</section>

<!-- Business card front -->
<section class="piece card-front" aria-label="Business card front">
  <svg class="art" viewBox="0 0 234 134" preserveAspectRatio="none">
    <path d="M0 8 C20 6 38 8 50 12 L44 42 C30 38 15 38 0 40 Z" fill="#dcdcdc"/>
    <path d="M38 0 C30 45 55 100 96 134 L234 134 L234 0 Z" fill="var(--green)"/>
  </svg>
  <div class="brand brand-light" style="left:48px;top:30px;gap:5px">
    <i class="brand-square" style="width:16px;height:16px;background:#fff"></i>
    <div class="brand-name"><span style="font-size:15px">Vantor Crest</span><span style="font-size:9px;padding-left:6px">Capital</span></div>
  </div>
  <div class="card-url">www.website.com</div>
</section>

<!-- Business card back -->
<section class="piece card-back" aria-label="Business card back">
  <svg class="art" viewBox="0 0 233 134" preserveAspectRatio="none">
    <path d="M86 0 C100 50 150 85 200 100 L0 120 L0 100 C50 90 70 50 86 0 Z" fill="#ececec"/>
    <path d="M86 0 L233 0 L233 88 C190 92 150 80 125 60 C105 42 92 22 86 0 Z" fill="var(--green)"/>
  </svg>
  <div class="brand" style="left:6px;top:10px;gap:4px">
    <i class="brand-square" style="width:11px;height:11px"></i>
    <div class="brand-name"><span style="font-size:9px">Vantor Crest</span><span style="font-size:5.5px;padding-left:4px">Capital</span></div>
  </div>
  <div class="person" style="right:8px;top:64px">
    <div class="name" style="font-size:9px;font-weight:400;color:#cfe8cf">Hale Marcus</div>
    <div class="role" style="font-size:6px;color:#cfe8cf">Executive</div>
  </div>
  <div class="contact-row" style="left:-10px;top:114px;font-size:6px">
    <div class="col" style="padding:0 7px">00, Address Line<br>Address Line 2</div>
    <div class="col" style="padding:0 7px">Phone: 000 XXX 0000<br>Fax: 000 XXX 0000</div>
    <div class="col" style="padding:0 7px">info@websitecom<br>www.websitecom</div>
  </div>
</section>

</body>
</html>
```